BrivoPeak Business Card Design Project

We are looking for a modern, clean business card design for our new company. We are a consulting firm focused on the financial services market providing management and IT consulting to banks, insurance companies, etc. Please include our company logo and company contact information from the attached file in the design. Two versions of the logo are attached, either version is acceptable. Logos are available in other file formats if needed. We would like to include the contact information for both our UK and US offices as well as the following information for each individual card holder: Name, position/title, address, phone number and e-mail address.
Updates
Project Deadline Extended
Reason: A last minute trip over seas has prevented us from finalizing the decision. A decision will be made this week. We apologize for the inconvenience.
Industry/Entity Type
Business
Contact Information for Business Card
Company logo.
Company locations and phone numbers for both the US and UK offices.
Company URL.
Cardholder Name
Cardholder Position/title
Cardholder Address
Cardholder Phone Number
Cardholder e-mail Address
Look and feel
Each slider illustrates characteristics of the customer's brand and the style your logo design should communicate.

```html
<!DOCTYPE html>
<html lang="en">
<head>
<meta charset="utf-8">
<title>BrivoPeak Business Cards</title>
<link href="https://fonts.googleapis.com/css2?family=Open+Sans:wght@400;600;700&display=swap" rel="stylesheet">
<style>
  :root {
    --navy: #1e3560;
    --grey: #666666;
    --grey-light: #8a8a8a;
    --card: #ffffff;
    --backdrop: #2b2b2b;
  }
  html, body {
    margin: 0;
    padding: 0;
    width: 1200px;
    height: 900px;
    overflow: hidden;
    background: var(--backdrop);
    font-family: "Open Sans", Arial, sans-serif;
  }
  .canvas {
    position: relative;
    width: 1200px;
    height: 900px;
  }
  .card {
    position: absolute;
    width: 680px;
    height: 388px;
    background: var(--card);
    box-shadow: 0 12px 30px rgba(0,0,0,0.45);
    overflow: hidden;
  }
  .card--front { left: 70px; top: 50px; }
  .card--back { left: 450px; top: 470px; }

  .brand {
    display: flex;
    align-items: center;
    gap: 12px;
  }
  .brand__mark {
    background: var(--navy);
  }
  .brand__name {
    color: var(--navy);
    font-weight: 700;
    letter-spacing: -0.5px;
  }

  /* Front */
  .card--front .brand {
    position: absolute;
    left: 60px;
    top: 60px;
  }
  .card--front .brand__name { font-size: 64px; line-height: 1; }
  .card--front .brand__mark { width: 22px; height: 22px; }
  .offices {
    position: absolute;
    left: 60px;
    bottom: 48px;
    font-size: 14px;
    line-height: 19px;
  }
  .office + .office { margin-top: 4px; }
  .office__line { color: var(--navy); }
  .office__phone { color: var(--grey-light); }
  .front-site {
    position: absolute;
    right: 50px;
    bottom: 48px;
    font-size: 14px;
    color: var(--navy);
  }

  /* Back */
  .card--back .brand {
    position: absolute;
    right: 44px;
    top: 40px;
  }
  .card--back .brand__name { font-size: 32px; line-height: 1; }
  .card--back .brand__mark { width: 14px; height: 14px; }
  .holder {
    position: absolute;
    right: 44px;
    top: 120px;
    text-align: right;
  }
  .holder__name {
    color: var(--navy);
    font-weight: 700;
    font-size: 22px;
    letter-spacing: 0.5px;
    margin: 0;
  }
  .holder__title {
    color: var(--grey-light);
    font-size: 12px;
    letter-spacing: 1px;
    margin: 0 0 14px;
  }
  .contact-list {
    list-style: none;
    margin: 0;
    padding: 0;
    font-size: 13px;
    line-height: 19px;
    color: var(--navy);
  }
  .contact-list li {
    display: flex;
    justify-content: flex-end;
    align-items: center;
    gap: 8px;
  }
  .contact-list svg {
    width: 11px;
    height: 11px;
    fill: none;
    stroke: var(--grey);
    stroke-width: 1.6;
  }
  .address-band {
    position: absolute;
    left: 0;
    bottom: 0;
    width: 430px;
    height: 70px;
    background: var(--grey);
    clip-path: polygon(0 0, 100% 0, 88% 100%, 0 100%);
  }
  .address-band__text {
    position: absolute;
    left: 26px;
    bottom: 14px;
    color: #ffffff;
    font-size: 14px;
    line-height: 19px;
  }
</style>
</head>
<body>
<main class="canvas">

  <section class="card card--front" aria-label="Business card front">
    <div class="brand">
      <span class="brand__name">BrivoPeak</span>
      <span class="brand__mark"></span>
    </div>
    <div class="offices">
      <div class="office">
        <div class="office__line">418 N Maple Row, Suite 204-117</div>
        <div class="office__line">Fairview UT 84630 United States</div>
        <div class="office__phone">US (801) 555-0142</div>
      </div>
      <div class="office">
        <div class="office__line">14-16 Harrow Lane</div>
        <div class="office__line">London E2 9QT Great Britain</div>
        <div class="office__phone">UK +44 7700 900412</div>
      </div>
    </div>
    <div class="front-site">www.brivopeakpartners.com</div>
  </section>

  <section class="card card--back" aria-label="Business card back">
    <div class="brand">
      <span class="brand__name">BrivoPeak</span>
      <span class="brand__mark"></span>
    </div>
    <div class="holder">
      <p class="holder__name">JONAS FELDBERG</p>
      <p class="holder__title">DIRECTOR</p>
      <ul class="contact-list">
        <li>(801) 555-0142
          <svg viewBox="0 0 12 12"><path d="M3 1 L5 3 L4 5 Q5.5 7 7 8 L9 7 L11 9 L9.5 11 Q4 10 1 3 Z"/></svg></li>
        <li>+44 7700 900412
          <svg viewBox="0 0 12 12"><rect x="2" y="6" width="8" height="5" rx="1"/><path d="M1 5 Q6 0 11 5"/></svg></li>
        <li>jonas@corvantisgroup.com
          <svg viewBox="0 0 12 12"><rect x="1" y="2.5" width="10" height="7"/><path d="M1 2.5 L6 7 L11 2.5"/></svg></li>
        <li>www.brivopeakpartners.com
          <svg viewBox="0 0 12 12"><circle cx="6" cy="6" r="5"/><ellipse cx="6" cy="6" rx="2" ry="5"/><path d="M1 6 H11"/></svg></li>
      </ul>
    </div>
    <div class="address-band">
      <div class="address-band__text">
        <div>3207-12 Birchmount</div>
        <div>Toronto, Ontario UK</div>
      </div>
    </div>
  </section>

</main>
</body>
</html>
```